Cool business cards

Use my existing logo from sketch harbor (see images I have uploaded) and design a really cool non-stuffy business card. I am a divorce mediator.

```html
<!DOCTYPE html>
<html lang="en">
<head>
<meta charset="utf-8">
<title>Morgan Ellery, J.D. — Business Cards</title>
<link href="https://fonts.googleapis.com/css2?family=Montserrat:wght@700&family=Questrial&display=swap" rel="stylesheet">
<style>
  :root {
    --canvas: #eeeae4;
    --brand-blue: #0e66b0;
    --brand-orange: #f47f20;
    --card-white: #ffffff;
    --text-grey: #7a7a7a;
    --icon-grey: #8c8c8c;
    --rule-grey: #b5b5b5;
  }
  * { box-sizing: border-box; margin: 0; padding: 0; }
  html, body {
    width: 1200px; height: 993px; overflow: hidden;
    background: var(--canvas);
  }
  .sheet {
    position: relative; width: 1200px; height: 993px;
    display: flex; align-items: center; justify-content: center; gap: 60px;
  }
  .card {
    position: relative; width: 525px; height: 300px;
    box-shadow: 0 6px 18px rgba(0,0,0,0.12);
  }
  .card--front { background: var(--brand-blue); }
  .card--back { background: var(--card-white); }

  .lockup {
    position: absolute; display: flex; flex-direction: column; align-items: center;
  }
  .card--front .lockup { left: 0; right: 0; top: 72px; }
  .card--back .lockup { left: 40px; width: 230px; top: 100px; }

  .lockup__dot {
    width: 78px; height: 78px; border-radius: 50%;
    background: var(--brand-orange);
    margin-bottom: 14px;
  }
  .card--back .lockup__dot { width: 66px; height: 66px; margin-bottom: 12px; }

  .lockup__name {
    font-family: "Montserrat", sans-serif; font-weight: 700;
    font-size: 25px; letter-spacing: 0.5px; color: var(--card-white);
    white-space: nowrap;
  }
  .card--back .lockup__name { color: var(--brand-blue); font-size: 17px; }

  .lockup__tagline {
    display: flex; align-items: center; gap: 8px; margin-top: 4px;
    font-family: "Montserrat", sans-serif; font-weight: 700;
    font-size: 8.5px; letter-spacing: 0.6px; color: #d6e3f0; white-space: nowrap;
  }
  .card--back .lockup__tagline { color: var(--text-grey); font-size: 6.5px; }
  .lockup__tagline::before, .lockup__tagline::after {
    content: ""; width: 22px; height: 1px; background: currentColor;
  }

  .card__holder {
    position: absolute; top: 48px; left: 276px;
    font-family: "Questrial", sans-serif; font-size: 15px;
    color: var(--text-grey); letter-spacing: 0.5px;
  }
  .contact {
    position: absolute; left: 282px; top: 162px; list-style: none;
    display: flex; flex-direction: column; gap: 12px;
  }
  .contact__item {
    display: flex; align-items: center; gap: 10px;
    font-family: "Questrial", sans-serif; font-size: 15.5px; color: var(--text-grey);
  }
  .contact__icon { width: 15px; height: 15px; fill: var(--icon-grey); flex: none; }
</style>
</head>
<body>
<main class="sheet">
  <section class="card card--front" aria-label="Card front">
    <div class="lockup">
      <span class="lockup__dot" aria-hidden="true"></span>
      <span class="lockup__name">MORGAN ELLERY, J.D.</span>
      <span class="lockup__tagline">DIVORCE &amp; FAMILY MEDIATION</span>
    </div>
  </section>

  <section class="card card--back" aria-label="Card back">
    <p class="card__holder">NAME</p>
    <div class="lockup">
      <span class="lockup__dot" aria-hidden="true"></span>
      <span class="lockup__name">MORGAN ELLERY, J.D.</span>
      <span class="lockup__tagline">DIVORCE &amp; FAMILY MEDIATION</span>
    </div>
    <ul class="contact">
      <li class="contact__item">
        <svg class="contact__icon" viewBox="0 0 24 24" aria-hidden="true"><path d="M6.6 10.8a15.1 15.1 0 0 0 6.6 6.6l2.2-2.2c.3-.3.7-.4 1-.2 1.1.4 2.3.6 3.6.6.6 0 1 .4 1 1V20c0 .6-.4 1-1 1C10.6 21 3 13.4 3 4c0-.6.4-1 1-1h3.5c.6 0 1 .4 1 1 0 1.3.2 2.5.6 3.6.1.3 0 .7-.2 1z"/></svg>
        +00 000000000
      </li>
      <li class="contact__item">
        <svg class="contact__icon" viewBox="0 0 24 24" aria-hidden="true"><path d="M2 5h20v14H2z M4 7v.3l8 5.2 8-5.2V7z" fill-rule="evenodd"/></svg>
        name@morganellery.com
      </li>
      <li class="contact__item">
        <svg class="contact__icon" viewBox="0 0 24 24" aria-hidden="true"><path fill="none" stroke="#8c8c8c" stroke-width="1.8" d="M12 2.5a9.5 9.5 0 1 0 0 19 9.5 9.5 0 1 0 0-19zM2.5 12h19M12 2.5c-3 3-3 16 0 19M12 2.5c3 3 3 16 0 19M4.5 7h15M4.5 17h15"/></svg>
        www.morganellery.com
      </li>
    </ul>
  </section>
</main>
</body>
</html>
```